Technology Company Needs a Brochure Design

We are a company which develops products and services for the monitoring of earthquakes in mines.

We need a product brochure for a new range of sensors we are developing. The brochure needs to convey to the user the important technical specifications of the new range of sensors.

We provide all content (text, images, etc.) as a PDF document with very basic layout, but your job is to choose the font, layout and composition of the brochure as well as colour scheme backround images, etc.

We are looking for a clean uncluttered high-tech look and feel. The main challenge will be getting a lot of text and images onto a page or two without feeling cluttered and like a standard word document.

Target Market(s)

Geotechnical Engineers, Electronic Engineers, Mine Managers

Industry/Entity Type

It Company

Font styles to use
Sans Serif

Colors
0255a3

Requirements
Must have
• You MUST include all text and images as per the attached PDF. This is an absolute minimum.
• You should choose a font, size, composition and general brochure layout, including colour scheme, background images/watermarks/headers/footers as you see fit so that the end product looks great.
• Re-arrange the text and images as necessary, e.g. into columns or across multiple pages so achieve the best result.
Nice to have
• Technology look and feel. Dark blues and greys in colour scheme. Clean uncluttered composition.
Should not have
• The brochure will mostly be electronic, and seldom printed, so we are not interested in a cover or back page just the main content.

```html
<!DOCTYPE html>
<html lang="en">
<head>
<meta charset="utf-8">
<title>RSI Hybrid and WGM Sensors – Brochure</title>
<link rel="stylesheet" href="https://fonts.googleapis.com/css2?family=Open+Sans:wght@400;600&family=Ubuntu:wght@400;500&display=swap">
<style>
:root{
  --blue:#0255a3;
  --navy:#0d2a6b;
  --red:#e0262a;
  --green:#2aa84a;
  --ink:#4a4a4a;
  --grey:#5e6166;
  --rule:#c9ced6;
  --stage:#e9ebee;
  --paper:#ffffff;
}
*{box-sizing:border-box;margin:0;padding:0}
html,body{width:1200px;height:1200px;overflow:hidden;background:var(--stage)}
body{position:relative;font-family:"Open Sans",Arial,sans-serif;color:var(--ink)}
.page{position:absolute;top:218px;width:541px;height:765px;background:var(--paper);overflow:hidden;box-shadow:0 4px 18px rgba(0,0,0,.25)}
.page--left{left:44px;background:linear-gradient(180deg,#eef1f5 0,#fff 300px)}
.page--right{left:616px}
.page-art{position:absolute;left:0;top:0;width:541px;height:765px}
.hero-illustration{position:absolute;left:215px;top:8px;width:326px;height:200px;background:linear-gradient(180deg,#f4f6f9 0%,#e2e7ef 45%,#c9d2e2 55%,#eef1f5 100%)}
.brand{position:absolute;display:flex;align-items:center;gap:12px}
.brand-dot{width:50px;height:50px;border-radius:50%;background:var(--blue);flex:none}
.brand-name{font-family:"Ubuntu",Arial,sans-serif;font-weight:400;font-size:19px;line-height:19px;color:var(--grey);border-left:1px solid var(--rule);padding-left:8px}
.page--left .brand{left:38px;top:42px}
.page--right .brand{left:20px;top:32px}
.hero-kicker{position:absolute;left:20px;top:232px;font-family:"Ubuntu",Arial,sans-serif;font-weight:500;font-size:30px;color:var(--grey)}
.hero-title{position:absolute;left:20px;top:268px;font-family:"Ubuntu",Arial,sans-serif;font-size:20px;color:var(--blue)}
.page-title{position:absolute;left:20px;top:302px;width:238px;font-family:"Ubuntu",Arial,sans-serif;font-weight:500;font-size:17.5px;color:var(--grey);padding-bottom:5px;border-bottom:1px solid var(--rule)}
.col{position:absolute;width:238px}
h3{font-family:"Ubuntu",Arial,sans-serif;font-weight:500;font-size:10.5px;color:var(--blue);margin-bottom:5px}
p{font-size:7.1px;line-height:9.7px;text-align:justify;color:var(--ink);margin-bottom:7px}
.wide{position:absolute;left:19px;width:503px}
.chart{position:absolute;width:238px;height:172px;border:1px solid var(--rule);background:#fff}
.chart svg{width:100%;height:100%;display:block}
.chart text{font-family:"Open Sans",Arial,sans-serif;fill:#333}
.photo{position:absolute;left:19px;top:227px;width:238px;height:170px;background:radial-gradient(circle at 45% 60%,#e3b89e 0%,#c38e73 30%,#4a3a32 75%,#1e1a18 100%)}
.footer{position:absolute;left:0;top:729px;width:541px;height:25px;background:var(--blue);display:flex;align-items:center;justify-content:space-between;padding:0 20px}
.footer-item{display:flex;align-items:center;gap:4px;color:#fff;font-size:7.6px}
.footer-item svg{width:10px;height:10px}
.conclusion-title{position:absolute;left:19px;top:663px;font-family:"Ubuntu",Arial,sans-serif;font-weight:500;font-size:11px;color:var(--blue)}
</style>
</head>
<body>

<section class="page page--left">
  <div class="hero-illustration" role="img" aria-label="Seismogram illustration: a tall dark blue waveform burst with a red trace running through it"></div>
  <svg class="page-art" viewBox="0 0 541 765" aria-hidden="true">
    <polygon points="3,222 150,157 246,238" fill="var(--blue)"/>
    <polygon points="150,157 246,238 200,245 110,190" fill="var(--navy)" opacity=".9"/>
    <polygon points="200,245 246,238 330,210 300,250" fill="#dfe5ee"/>
    <polygon points="330,235 388,212 541,306 541,332 430,265" fill="var(--blue)"/>
    <polygon points="388,212 541,290 541,306" fill="var(--navy)"/>
  </svg>

  <div class="brand"><span class="brand-dot"></span><span class="brand-name">rockline<br>seismic<br>institute</span></div>

  <div class="hero-kicker">We are the</div>
  <div class="hero-title">Rockline Seismic Institute</div>
  <div class="page-title">RSI Hybrid and WGM Sensors</div>

  <div class="col" style="left:20px;top:340px">
    <h3>Limitations of conventional sensors</h3>
    <p>For decades, miniature geophones and integrated electronic piezoelectric (IEPE) accelerometers have been the sensors of choice for microseismic monitoring in mines. Which of these sensors to use is not always an obvious decision - there are clear advantages and disadvantages to both. IEPE accelerometers are more sensitive to higher frequencies, and so are better suited to denser arrays monitoring smaller seismic events occurring closer to the sensors.</p>
    <p>They are also less sensitive to the low frequencies generated by larger events, but saturate more easily on the higher frequencies of even moderately sized events. Geophones have a lower noise floor (and higher dynamic range) over most of their usable bandwidth, but clip more easily due to the large displacements of nearby large events. These concepts are illustrated in the following theoretical graphs, where shaded regions indicate one sensor outperforming the other.</p>
  </div>

  <div class="col" style="left:284px;top:304px">
    <h3>Hybrid Sensors</h3>
    <p>RSI now offers hybrid sensors where both types of sensor can be included in a single sensor package. Combining the complementary characteristics of geophones and IEPE accelerometers means that better coverage of a wider variety of seismic events is achievable, which ultimately results in higher quality of the seismic event catalogue.</p>
    <h3>Clipping and Saturation</h3>
    <p>A common problem with both of these traditional seismic sensors is their limited upper measurement range. Geophones typically clip at ground displacements above a few millimetres, and IEPE accelerometers saturate at ground accelerations above a few tens of g's. Adding to this, when the signal from these sensors is outside of the recorder's analogue-to-digital converter (ADC) voltage range, an additional type of non-linear signal distortion is introduced. All this means that the ground motions of large and/or nearby seismic events cannot be accurately recorded. This is a serious problem because large (often damaging) events are not able to be properly analysed, which makes back-analysis, seismic hazard assessments and other seismological work more difficult.</p>
  </div>

  <figure class="chart" style="left:20px;top:536px">
    <svg viewBox="0 0 238 172">
      <text x="119" y="14" font-size="6.5" text-anchor="middle">Accelerometer vs Geophone Dynamic Range</text>
      <rect x="34" y="28" width="188" height="123" fill="none" stroke="#999" stroke-width=".5"/>
      <polygon points="34,38 110,68 34,60" fill="#9aa3f0" opacity=".7"/>
      <polygon points="110,68 222,40 222,96" fill="#f7a3a3" opacity=".7"/>
      <polygon points="34,98 150,140 222,145 222,120" fill="#f7a3a3" opacity=".6"/>
      <line x1="34" y1="38" x2="222" y2="96" stroke="var(--blue)" stroke-width="1"/>
      <path d="M34,60 Q70,75 110,68 L222,40" fill="none" stroke="var(--red)" stroke-width="1"/>
      <line x1="34" y1="98" x2="222" y2="145" stroke="var(--blue)" stroke-width="1" stroke-dasharray="3,2"/>
      <path d="M34,110 Q60,138 110,140 Q170,142 222,120" fill="none" stroke="var(--red)" stroke-width="1" stroke-dasharray="3,2"/>
      <g font-size="4.6" text-anchor="end">
        <text x="180" y="86">Geophone Clip Limit</text>
        <text x="180" y="92">Geophone Noise (Broadband, RMS)</text>
        <text x="180" y="98">Accelerometer Limit</text>
        <text x="180" y="104">Accelerometer Noise (Broadband, RMS)</text>
      </g>
      <line x1="183" y1="84" x2="195" y2="84" stroke="var(--red)"/>
      <line x1="183" y1="90" x2="195" y2="90" stroke="var(--red)" stroke-dasharray="2,1"/>
      <line x1="183" y1="96" x2="195" y2="96" stroke="var(--blue)"/>
      <line x1="183" y1="102" x2="195" y2="102" stroke="var(--blue)" stroke-dasharray="2,1"/>
      <text x="128" y="163" font-size="6" text-anchor="middle">Frequency [Hz]</text>
      <text x="16" y="90" font-size="5.5" text-anchor="middle" transform="rotate(-90 16 90)">Ground Velocity [m/s]</text>
    </svg>
  </figure>

  <figure class="chart" style="left:284px;top:536px">
    <svg viewBox="0 0 238 172">
      <text x="119" y="13" font-size="6" text-anchor="middle">IEPE Accelerometer and Geophone</text>
      <text x="119" y="21" font-size="6" text-anchor="middle">Normalised Sensitivity vs Frequency Response</text>
      <rect x="38" y="28" width="184" height="123" fill="none" stroke="#999" stroke-width=".5"/>
      <line x1="38" y1="33" x2="222" y2="33" stroke="#333" stroke-width=".4" stroke-dasharray="1,1"/>
      <line x1="38" y1="45" x2="222" y2="45" stroke="#333" stroke-width=".4" stroke-dasharray="1,1"/>
      <path d="M38,60 Q50,40 80,38 L108,38 Q80,70 38,145 Z" fill="#9aa3f0" opacity=".7"/>
      <path d="M190,38 L222,34 L222,80 Q212,50 190,38 Z" fill="#9aa3f0" opacity=".7"/>
      <path d="M38,60 Q50,40 80,38 L222,34" fill="none" stroke="var(--blue)" stroke-width="1.1"/>
      <path d="M38,145 Q80,70 108,38 L190,38 Q212,50 222,80" fill="none" stroke="var(--red)" stroke-width="1.1"/>
      <g font-size="4.8" text-anchor="end">
        <text x="178" y="95">IEPE Accelerometer [V/m/s²]</text>
        <text x="178" y="101">Geophone [V/m/s]</text>
      </g>
      <line x1="181" y1="93" x2="193" y2="93" stroke="var(--blue)"/>
      <line x1="181" y1="99" x2="193" y2="99" stroke="var(--red)"/>
      <text x="130" y="163" font-size="6" text-anchor="middle">Frequency [Hz]</text>
      <text x="18" y="90" font-size="5.5" text-anchor="middle" transform="rotate(-90 18 90)">Normalised Sensitivity [dB]</text>
    </svg>
  </figure>

  <footer class="footer">
    <span class="footer-item"><svg viewBox="0 0 10 10"><path d="M1 3 Q5 0 9 3 L8 4.5 L6.5 3.5 L3.5 3.5 L2 4.5 Z M2 5 h6 v4 h-6 z" fill="#fff"/></svg>+10 55 0142270</span>
    <span class="footer-item"><svg viewBox="0 0 10 10"><path d="M1 3 Q5 0 9 3 L8 4.5 L2 4.5 Z M2 5 h6 v4 h-6 z M3 6 h4 v1 h-4z" fill="#fff"/></svg>+10 55 0142271</span>
    <span class="footer-item"><svg viewBox="0 0 10 10"><rect x="1" y="2" width="8" height="6" fill="none" stroke="#fff" stroke-width=".9"/><path d="M1 2 L5 5.5 L9 2" fill="none" stroke="#fff" stroke-width=".9"/></svg>info@rocklineseismic.org</span>
    <span class="footer-item"><svg viewBox="0 0 10 10"><circle cx="5" cy="5" r="4" fill="none" stroke="#fff" stroke-width=".9"/><ellipse cx="5" cy="5" rx="1.8" ry="4" fill="none" stroke="#fff" stroke-width=".7"/><line x1="1" y1="5" x2="9" y2="5" stroke="#fff" stroke-width=".7"/></svg>www.rocklineseismic.org</span>
  </footer>
</section>

<section class="page page--right">
  <svg class="page-art" viewBox="0 0 541 765" aria-hidden="true">
    <polygon points="290,0 541,0 541,98" fill="#f2f4f7"/>
    <polygon points="185,0 290,0 541,98 541,130 450,78 370,88" fill="var(--blue)"/>
    <polygon points="260,0 290,0 370,88 330,70" fill="var(--navy)"/>
    <polygon points="450,78 541,98 541,130" fill="var(--navy)"/>
  </svg>

  <div class="brand"><span class="brand-dot"></span><span class="brand-name">rockline<br>seismic<br>institute</span></div>

  <div class="col" style="left:19px;top:120px">
    <h3>Wide-range Ground Motion (WGM) Sensors</h3>
    <p>For decades, miniature geophones and integrated electronic piezoelectric (IEPE) accelerometers have been the sensors of choice for microseismic monitoring in mines. Which of these sensors to use is not always an obvious decision - there are clear advantages and disadvantages to both. IEPE accelerometers are more sensitive to higher frequencies, and so are better suited to denser arrays monitoring smaller seismic events occurring closer to the sensors.</p>
  </div>

  <div class="col" style="left:284px;top:134px">
    <p>The figure on the left shows a signal trace recorded on a shake table where a 4.5 Hz geophone (blue trace) displays severe non-linearities due to a combination of ADC saturation and mechanical clipping during strong ground motions. The red trace shows the signal recorded by the MEMS accelerometer embedded inside a WGM sensor, which is clearly more representative of the true ground motion, displaying none of the non-linearities of the conventional geophone sensor.</p>
  </div>

  <div class="photo" role="img" aria-label="Close-up photograph of a tiny MEMS sensor chip resting on a fingertip"></div>

  <figure class="chart" style="left:284px;top:227px;height:170px">
    <svg viewBox="0 0 238 170">
      <text x="119" y="14" font-size="5.2" text-anchor="middle">Shake Table Comparison: MEMS vs Geophone, Velocity</text>
      <rect x="30" y="22" width="196" height="132" fill="none" stroke="#999" stroke-width=".5"/>
      <line x1="30" y1="62" x2="226" y2="62" stroke="#333" stroke-width=".4" stroke-dasharray="1,1"/>
      <line x1="30" y1="114" x2="226" y2="114" stroke="#333" stroke-width=".4" stroke-dasharray="1,1"/>
      <path d="M30,88 L44,88 q4.5,-60 9,0 t9,0 t9,0 t9,0 t9,0 t9,0 t9,0 t9,0 t9,0 t9,0 t9,0 t9,0 t9,0 t9,0 t9,0 t9,0 t9,0 t9,0 t9,0" fill="none" stroke="var(--red)" stroke-width="1"/>
      <path d="M30,88 L36,86 L40,90 L44,88 l1,-26 l1,18 l1,-10 l1.5,18 l1,26 l1,-18 l1,12 l1.5,-20 l1,-26 l1,18 l1,-10 l1.5,18 l1,26 l1,-18 l1,12 l1.5,-20 l1,-26 l1,18 l1,-10 l1.5,18 l1,26 l1,-18 l1,12 l1.5,-20 l1,-26 l1,18 l1,-10 l1.5,18 l1,26 l1,-18 l1,12 l1.5,-20 l1,-26 l1,18 l1,-10 l1.5,18 l1,26 l1,-18 l1,12 l1.5,-20 l1,-26 l1,18 l1,-10 l1.5,18 l1,26 l1,-18 l1,12 l1.5,-20 l1,-26 l1,18 l1,-10 l1.5,18 l1,26 l1,-18 l1,12 l1.5,-20 l1,-26 l1,18 l1,-10 l1.5,18 l1,26 l1,-18 l1,12 l1.5,-20 l1,-26 l1,18 l1,-10 l1.5,18 l1,26 l1,-18 l1,12 l1.5,-20 l1,-26 l1,18 l1,-10 l1.5,18 l1,26 l1,-18 l1,12 l1.5,-20 l1,-26 l1,18 l1,-10 l1.5,18 l1,26 l1,-18 l1,12 l1.5,-20 l1,-26 l1,18 l1,-10 l1.5,18 l1,26 l1,-18 l1,12 l1.5,-20 l1,-26 l1,18 l1,-10 l1.5,18 l1,26 l1,-18 l1,12 l1.5,-20 l1,-26 l1,18 l1,-10 l1.5,18 l1,26 l1,-18 l1,12 l1.5,-20 l1,-26 l1,18 l1,-10 l1.5,18 l1,26 l1,-18 l1,12 l1.5,-20 l1,-26 l1,18 l1,-10 l1.5,18 l1,26 l1,-18 l1,12 l1.5,-20 l1,-26 l1,18 l1,-10 l1.5,18 l1,26 l1,-18 l1,12 l1.5,-20 l1,-26 l1,18 l1,-10 l1.5,18 l1,26 l1,-18 l1,12 l1.5,-20" fill="none" stroke="var(--blue)" stroke-width=".8"/>
      <g font-size="3.8" text-anchor="end">
        <text x="210" y="29">Geophone z component (8000 sps sample rate)</text>
        <text x="210" y="34">MEMS z component integrated (800 sps sample rate)</text>
        <text x="210" y="39">ADC Saturation Limits</text>
      </g>
      <line x1="212" y1="28" x2="222" y2="28" stroke="var(--blue)" stroke-width=".7"/>
      <line x1="212" y1="33" x2="222" y2="33" stroke="var(--red)" stroke-width=".7"/>
      <line x1="212" y1="38" x2="222" y2="38" stroke="#333" stroke-width=".5" stroke-dasharray="1,1"/>
      <text x="128" y="163" font-size="4.5" text-anchor="middle">Time [s]</text>
      <text x="14" y="88" font-size="4.2" text-anchor="middle" transform="rotate(-90 14 88)">Ground Velocity [m/s]</text>
    </svg>
  </figure>

  <p class="wide" style="top:418px">Every seismic sensor manufactured by RSI, whether geophone, accelerometer or a hybrid combination, now includes WGM sensors. The WGM sensor is able to record the strong ground motions which conventional sensors and ADCs cannot, and because they are sensitive to frequencies down to DC, they will also be capable of recording lower frequency signals. The following figures illustrate these concepts, where shaded regions indicate one sensor outperforming the other. The effective result of the composite WGM sensor is the combination of all shaded regions.</p>

  <figure class="chart" style="left:19px;top:474px;height:170px">
    <svg viewBox="0 0 238 170">
      <text x="119" y="17" font-size="6.5" text-anchor="middle">RSI WGM + 14 Hz Geophone Sensor</text>
      <text x="119" y="26" font-size="6.5" text-anchor="middle">Frequency Response and Dynamic Range</text>
      <rect x="48" y="36" width="176" height="110" fill="none" stroke="#999" stroke-width=".5"/>
      <polygon points="48,40 175,70 175,103 48,85" fill="#9fe0ae" opacity=".8"/>
      <polygon points="48,85 140,95 175,70 175,120 140,112 48,92" fill="#f7a3a3" opacity=".8"/>
      <line x1="48" y1="40" x2="224" y2="85" stroke="var(--green)" stroke-width="1"/>
      <path d="M48,85 L140,95 L175,70 L224,58" fill="none" stroke="var(--red)" stroke-width="1"/>
      <line x1="175" y1="70" x2="175" y2="120" stroke="#555" stroke-width=".5"/>
      <g font-size="4.6" text-anchor="end">
        <text x="200" y="132">Geophone Sensitive Region</text>
        <text x="200" y="138">WGM (MEMS Accelerometer) Sensitive Region</text>
      </g>
      <rect x="203" y="128" width="10" height="4" fill="#f7a3a3"/>
      <rect x="203" y="134" width="10" height="4" fill="#9fe0ae"/>
      <text x="136" y="158" font-size="6.5" text-anchor="middle">Frequency [Hz]</text>
      <text x="30" y="92" font-size="6" text-anchor="middle" transform="rotate(-90 30 92)">Ground motion [m/s]</text>
    </svg>
  </figure>

  <figure class="chart" style="left:284px;top:474px;height:170px">
    <svg viewBox="0 0 238 170">
      <text x="119" y="15" font-size="6" text-anchor="middle">Piezoelectric/MEMS Accelerometer vs Geophone</text>
      <text x="119" y="23" font-size="6" text-anchor="middle">Normalised Frequency Response</text>
      <rect x="42" y="30" width="182" height="118" fill="none" stroke="#999" stroke-width=".5"/>
      <line x1="42" y1="33" x2="224" y2="33" stroke="#333" stroke-width=".4" stroke-dasharray="1,1"/>
      <line x1="42" y1="44" x2="224" y2="44" stroke="#333" stroke-width=".4" stroke-dasharray="1,1"/>
      <path d="M42,36 L110,38 Q90,42 80,40 Q60,42 42,60 Z" fill="#9fe0ae" opacity=".8"/>
      <path d="M42,60 Q60,42 80,40 Q100,80 42,145 Z M190,40 L224,34 L224,86 Q212,52 190,40 Z" fill="#9aa3f0" opacity=".8"/>
      <line x1="42" y1="36" x2="224" y2="38" stroke="var(--green)" stroke-width="1"/>
      <path d="M42,60 Q60,42 80,39 L224,35" fill="none" stroke="var(--blue)" stroke-width="1"/>
      <path d="M42,145 Q80,70 108,38 L188,38 Q212,52 224,86" fill="none" stroke="var(--red)" stroke-width="1"/>
      <g font-size="4.6" text-anchor="end">
        <text x="180" y="90">MEMS Accelerometer [V/m/s²]</text>
        <text x="180" y="96">Piezoelectric Accelerometer [V/m/s²]</text>
        <text x="180" y="102">Geophone [V/m/s]</text>
      </g>
      <line x1="183" y1="88" x2="195" y2="88" stroke="var(--green)"/>
      <line x1="183" y1="94" x2="195" y2="94" stroke="var(--blue)"/>
      <line x1="183" y1="100" x2="195" y2="100" stroke="var(--red)"/>
      <text x="133" y="160" font-size="6" text-anchor="middle">Frequency [Hz]</text>
      <text x="22" y="90" font-size="5.5" text-anchor="middle" transform="rotate(-90 22 90)">Normalised Sensitivity [dB]</text>
    </svg>
  </figure>

  <div class="conclusion-title">Conclusion :</div>
  <p class="wide" style="top:681px">RSI has widened its sensor offering to include hybrid geophone / IEPE accelerometer combinations, and all sensors will now include embedded WGM functionality to enable the recording of high amplitude and/or low frequency seismic signals. Together, these enhancements enable more accurate, efficient and advanced seismological investigations including large event back-analyses and seismic hazard assessments.</p>

  <footer class="footer">
    <span class="footer-item"><svg viewBox="0 0 10 10"><path d="M1 3 Q5 0 9 3 L8 4.5 L6.5 3.5 L3.5 3.5 L2 4.5 Z M2 5 h6 v4 h-6 z" fill="#fff"/></svg>+10 55 0142270</span>
    <span class="footer-item"><svg viewBox="0 0 10 10"><path d="M1 3 Q5 0 9 3 L8 4.5 L2 4.5 Z M2 5 h6 v4 h-6 z M3 6 h4 v1 h-4z" fill="#fff"/></svg>+10 55 0142271</span>
    <span class="footer-item"><svg viewBox="0 0 10 10"><rect x="1" y="2" width="8" height="6" fill="none" stroke="#fff" stroke-width=".9"/><path d="M1 2 L5 5.5 L9 2" fill="none" stroke="#fff" stroke-width=".9"/></svg>info@rocklineseismic.org</span>
    <span class="footer-item"><svg viewBox="0 0 10 10"><circle cx="5" cy="5" r="4" fill="none" stroke="#fff" stroke-width=".9"/><ellipse cx="5" cy="5" rx="1.8" ry="4" fill="none" stroke="#fff" stroke-width=".7"/><line x1="1" y1="5" x2="9" y2="5" stroke="#fff" stroke-width=".7"/></svg>www.rocklineseismic.org</span>
  </footer>
</section>

</body>
</html>
```